Zerovan Medical

We are a medical supplier company we sell machines and equipment to all medical sectors in Iraq. Our services include not only the installation of these machines and equipment but also we provide support after installation and we train the staff to use these machines/equipment
We need a website that will make us stand out from our competitors, something professional and catchy
Starting from the home page, before showing the home page we want the loading screen to have our logo animated in a nice way
Then we can proceed to creating the other pages which are
Projects
Services
Training
About
and Contact us
Attached below is our logo and the color blue that we hope to use in the theme of the website
**** In the home page we want to focus on our partners and services****

Target Market(s)

Medical Sector

Industry/Entity Type

Medical

Coding

Coded - Design and coding required

Number of Pages Required

5+ page

Colors
0054AA
0677BA
7BADD7
CADEEF
E8F1F8

Requirements
Must have
• Animation in loading screen or animation in home page
Nice to have
• Some sort of animation for our partners

```html
<!DOCTYPE html>
<html lang="en">
<head>
<meta charset="UTF-8">
<title>Zerovan Medical — Trusted Partner For Medical Supplies</title>
<link href="https://fonts.googleapis.com/css2?family=Lexend:wght@500;600;700&family=Poppins:wght@400;500;600&display=swap" rel="stylesheet">
<style>
:root{
  --blue:#0054AA;
  --blue-2:#0677BA;
  --blue-3:#7BADD7;
  --blue-4:#CADEEF;
  --blue-5:#E8F1F8;
  --navy:#1c1f5c;
  --hero:#2a2f86;
  --gray:#f3f4f6;
  --text:#4a4d63;
  --white:#ffffff;
}
*{box-sizing:border-box;margin:0;padding:0}
html,body{width:1200px;height:4087px;overflow:hidden}
body{font-family:'Poppins',sans-serif;color:var(--text);background:var(--white);position:relative}
h1,h2,h3,h4,.brand,.partner{font-family:'Lexend',sans-serif}
.abs{position:absolute}
.btn{position:absolute;display:flex;align-items:center;justify-content:center;background:var(--blue);color:#fff;font:600 12px 'Poppins',sans-serif;letter-spacing:.6px;text-transform:uppercase}
.label{font-size:13px;color:var(--blue);letter-spacing:.4px;text-transform:uppercase}
.title{color:var(--navy);font-weight:700;line-height:1.25}
.photo{position:absolute}

/* hero */
.hero{position:absolute;left:0;top:0;width:1200px;height:675px;background:linear-gradient(120deg,#33399a 0%,#2c3390 45%,#3a4aa8 100%)}
.nav .brand{position:absolute;left:112px;top:16px;display:flex;align-items:center;gap:8px;color:#fff;font-size:19px;font-weight:600}
.brand .mark{width:24px;height:24px;border:3px solid var(--blue-3)}
.nav ul{position:absolute;left:465px;top:22px;display:flex;gap:25px;list-style:none;font-size:11px;font-weight:500;color:#fff;text-transform:uppercase}
.hero .nav .phone{left:937px;top:12px;width:150px;height:37px;background:var(--blue-2);gap:8px;text-transform:none;font-size:12px;letter-spacing:0}
.hero .tag{left:112px;top:212px;height:25px;padding:0 12px;background:rgba(255,255,255,.14);color:#fff;font-size:13px;letter-spacing:1px;display:flex;align-items:center;gap:10px}
.hero .tag i{display:block;width:20px;height:1px;background:#fff}
.hero h1{left:112px;top:256px;color:#fff;font-size:51px;font-weight:600;line-height:62px}
.hero p{left:112px;top:400px;width:470px;color:#fff;font-size:16.5px;line-height:29px}
.hero .cta{left:112px;top:486px;width:165px;height:37px;background:var(--blue-2)}
.tile{position:absolute;background:#fff;border-radius:4px;box-shadow:0 10px 30px rgba(0,0,0,.25);display:flex;align-items:center;justify-content:center;color:#222;font-family:'Lexend',sans-serif;font-weight:500}

/* partners */
.partners{position:absolute;left:0;top:675px;width:1200px;height:150px;background:#fff}
.partners .lead{left:112px;top:52px;font-size:14px;font-weight:600;color:var(--navy);line-height:24px}
.partners .row{position:absolute;left:275px;top:60px;width:812px;display:flex;justify-content:space-between;align-items:center}
.partner{font-size:21px;font-weight:600;color:#2a2c44}

/* about */
.about{position:absolute;left:0;top:825px;width:1200px;height:540px;background:var(--gray)}
.about .back{left:111px;top:53px;width:241px;height:312px;background:#e1e3e8;border-radius:6px}
.about .photo{left:135px;top:75px;width:465px;height:389px;border-radius:12px;background:linear-gradient(135deg,#4a5ee0,#2d3fb4 55%,#7f90e8)}
.about h2{left:660px;top:112px;font-size:38px}
.about .label{position:absolute;left:660px;top:72px}
.about .copy{left:660px;top:219px;width:390px;font-size:12.5px;line-height:22px}
.about .copy p+p{margin-top:8px}
.about .btn{left:660px;top:425px;width:135px;height:39px}

/* services */
.services .label{position:absolute;left:0;width:1200px;top:1438px;text-align:center}
.services h2{left:0;width:1200px;top:1462px;text-align:center;font-size:39px}
.card{position:absolute;top:1579px;width:308px;height:306px;border-radius:8px;overflow:hidden}
.card .photo{inset:0}
.card h3{position:absolute;left:29px;bottom:26px;color:#fff;font-size:21px;font-weight:600}
.card > svg{position:absolute;left:29px}
.card.support .photo{background:linear-gradient(160deg,#5b5f8c,#45497a)}
.card.support h3{top:99px;bottom:auto}
.card.support p{position:absolute;left:29px;top:143px;width:250px;color:#e8e9f3;font-size:11.5px;line-height:19px}
.card .go{position:absolute;left:29px;top:249px;width:29px;height:29px;border-radius:50%;background:#fff;display:block}
.card .go svg{display:block}
.services .btn{left:517px;top:1917px;width:165px;height:39px}

/* training */
.training{position:absolute;left:0;top:2032px;width:1200px;height:503px;background:var(--gray)}
.training .label{position:absolute;left:112px;top:74px}
.training h2{left:112px;top:98px;font-size:38px}
.training p{left:112px;top:206px;width:460px;font-size:12.5px;line-height:21.7px}
.training .btn{left:112px;top:388px;width:165px;height:39px}

/* projects */
.projects .label{position:absolute;left:0;width:1200px;top:2607px;text-align:center}
.projects h2{left:0;width:1200px;top:2632px;text-align:center;font-size:39px}
.proj h4{position:absolute;font-size:22px;color:var(--navy);font-weight:600;top:3032px}
.proj p{position:absolute;top:3074px;width:410px;font-size:12.5px;line-height:19px}
.circ{position:absolute;width:36px;height:36px;border-radius:50%;display:flex;align-items:center;justify-content:center}

/* contact */
.contact{position:absolute;left:0;top:3180px;width:1200px;height:585px;background:linear-gradient(120deg,#2c4e8e,#1d3c7a 45%,#3867a7)}
.form{position:absolute;left:614px;top:78px;width:473px;height:432px;background:#fff;border-radius:10px}
.form .label{position:absolute;left:46px;top:48px}
.form h2{position:absolute;left:46px;top:76px;font-size:36px}
.field{position:absolute;height:39px;border:1px solid #dcdde3;font-size:11.5px;color:#333;padding:12px 14px}
.form .btn{left:46px;bottom:44px;width:90px;height:39px}

/* footer */
.footer .brand{position:absolute;left:111px;top:3816px;display:flex;align-items:center;gap:8px;color:var(--navy);font-size:16px;font-weight:600;white-space:nowrap}
.footer .brand .mark{border-color:var(--blue-2)}
.social{position:absolute;top:3880px;width:33px;height:33px;border-radius:50%;border:1px solid #9b9db0}
.col{position:absolute;top:3822px;font-size:12.5px;color:#444}
.col h4{font-size:16px;color:var(--navy);font-weight:600;margin-bottom:14px}
.col li{list-style:none;line-height:26px}
.contact-item{display:flex;gap:10px;line-height:20px;margin-bottom:8px}
.news{position:absolute;left:854px;top:3893px;width:233px;height:39px;border:1px solid #dcdde3;font-size:11.5px;padding:12px 14px;color:#333}
.news b{position:absolute;right:-1px;top:-1px;width:41px;height:39px;background:var(--navy);display:flex;align-items:center;justify-content:center}
.bottom{position:absolute;left:0;top:4040px;width:1200px;height:47px;background:var(--blue);color:#fff;font-size:12px;display:flex;align-items:center;justify-content:center}
</style>
</head>
<body>

<header class="hero">
  <div class="photo" role="img" aria-label="Blurred hospital imaging room in blue tones" style="inset:0;background:radial-gradient(ellipse at 60% 30%,rgba(120,140,220,.35),transparent 60%)"></div>
  <nav class="nav">
    <div class="brand"><span class="mark"></span>Zerovan Medical</div>
    <ul><li>Home</li><li>About</li><li>Services</li><li>Training</li><li>Projects</li><li>Contact Us</li></ul>
    <div class="btn phone">
      <svg width="14" height="14" viewBox="0 0 24 24" fill="none" stroke="#fff" stroke-width="2"><path d="M22 16.9v3a2 2 0 0 1-2.2 2 19.8 19.8 0 0 1-8.6-3.1 19.5 19.5 0 0 1-6-6A19.8 19.8 0 0 1 2.1 4.2 2 2 0 0 1 4.1 2h3a2 2 0 0 1 2 1.7c.1 1 .4 1.9.7 2.8a2 2 0 0 1-.5 2.1L8 9.9a16 16 0 0 0 6 6l1.3-1.3a2 2 0 0 1 2.1-.4c.9.3 1.8.6 2.8.7a2 2 0 0 1 1.7 2z"/></svg>
      (555) 0148-221
    </div>
  </nav>
  <div class="abs tag">Welcome to Zerovan Medical <i></i></div>
  <h1 class="abs">Trusted Partner For<br>Medical Supplies</h1>
  <p class="abs">We are a medical supplier company we sell machines and equipment to all medical sectors in Iraq.</p>
  <div class="btn cta">Contact Us Now</div>

  <div class="tile" role="img" aria-label="Operating theatre photo" style="left:636px;top:173px;width:127px;height:89px;background:linear-gradient(135deg,#c9d2e6,#8e9cbf)"></div>
  <div class="tile" style="left:843px;top:173px;width:127px;height:89px;font-size:20px;letter-spacing:6px">VELTRA</div>
  <div class="tile" style="left:741px;top:322px;width:127px;height:89px;font-size:18px">orbis</div>
  <div class="tile" style="left:960px;top:305px;width:172px;height:125px;font-size:18px;color:var(--blue-2)">Zerovan</div>
  <div class="tile" role="img" aria-label="MRI scanner photo" style="left:636px;top:473px;width:127px;height:90px;background:linear-gradient(135deg,#dfe6f2,#9fb0d0)"></div>
  <div class="tile" style="left:843px;top:473px;width:127px;height:90px;font-size:28px">lunor</div>
</header>

<section class="partners">
  <div class="abs lead">Get In-Network<br>Care With</div>
  <div class="row">
    <span class="partner">Lumora</span>
    <span class="partner">QUANTEX</span>
    <span class="partner">brightbox</span>
    <span class="partner" style="font-size:16px;letter-spacing:1.5px">MERIDIO</span>
    <span class="partner">vanta</span>
    <span class="partner">(atrium)</span>
  </div>
</section>

<section class="about">
  <div class="abs back"></div>
  <div class="photo" role="img" aria-label="Surgeons working under operating lights"></div>
  <div class="label">Welcome To</div>
  <h2 class="abs title">Al Zerovan For<br>Madical Appliances</h2>
  <div class="abs copy">
    <p>Lorem ipsum dolor sit amet, consectetuer adipiscing elit, sed diam nonummy nibh euismod tincidunt ut laoreet dolore magna aliquam erat volutpat.</p>
    <p>Ut wisi enim ad minim veniam, quis nostrud exerci tation ullamcorper suscipit lobortis nisl ut aliquip ex ea commodo consequat. Duis autem vel eum iriure dolor in hendrerit in vulputate velit esse molestie consequat, vel illum dolore eu feugiat nulla facilisis at vero eros.</p>
  </div>
  <div class="btn">Know More</div>
</section>

<section class="services">
  <div class="label">Our Services</div>
  <h2 class="abs title">Machines &amp; Equipment To All<br>Medical Sectors</h2>

  <div class="card" style="left:111px">
    <div class="photo" role="img" aria-label="Engineer installing a medical robot arm" style="background:linear-gradient(160deg,#8a8f9c,#3b3d48 60%,#c2682c)"></div>
    <svg style="top:200px" width="40" height="40" viewBox="0 0 40 40" fill="none" stroke="#fff" stroke-width="2"><circle cx="20" cy="20" r="7"/><circle cx="20" cy="20" r="14" stroke-dasharray="5 4"/></svg>
    <h3>Installation</h3>
  </div>
  <div class="card support" style="left:446px">
    <div class="photo" role="img" aria-label="Support agent with a headset"></div>
    <svg style="top:38px" width="40" height="44" viewBox="0 0 40 44" fill="none" stroke="#fff" stroke-width="2"><circle cx="20" cy="16" r="8"/><path d="M8 40c0-7 5-12 12-12s12 5 12 12"/><rect x="24" y="2" width="14" height="9" rx="2"/></svg>
    <h3>Support</h3>
    <p>Lorem ipsum dolor sit amet, contetuer adipiscing elit, sed diam nonummy nibh euismod tincidunt ut laoreet dolore magna aliquam erat volutpat.</p>
    <span class="go"><svg width="29" height="29" viewBox="0 0 29 29" fill="none" stroke="#333" stroke-width="2"><path d="M10 14.5h9M15 10.5l4 4-4 4"/></svg></span>
  </div>
  <div class="card" style="left:779px">
    <div class="photo" role="img" aria-label="Medical staff in a training session" style="background:linear-gradient(160deg,#6d7a96,#3d465e 60%,#7a8fb0)"></div>
    <svg style="top:196px" width="42" height="42" viewBox="0 0 42 42" fill="none" stroke="#fff" stroke-width="2"><rect x="14" y="4" width="24" height="18"/><circle cx="9" cy="14" r="4"/><path d="M3 38V24h12l6-6M9 38V30"/></svg>
    <h3>Training</h3>
  </div>
  <div class="btn">Contact Us Now</div>
</section>

<section class="training">
  <div class="label">Training</div>
  <h2 class="abs title">We Train The Staff To Use<br>These Machines</h2>
  <p class="abs">Lorem ipsum dolor sit amet, consectetuer adipiscing elit, sed diam nonummy nibh euismod tincidunt ut laoreet dolore magna aliquam erat volutpat. Ut wisi enim ad minim veniam, quis nostrud exerci tation ullamcorper suscipit lobortis nisl ut aliquip ex ea commodo consequat. Duis autem vel eum iriure dolor in hendrerit in vulputate velit esse molestie consequat, vel illum dolore eu feugiat nulla facilisis at vero eros.</p>
  <div class="btn">Get Training Now</div>
  <svg class="abs" style="left:680px;top:70px" width="430" height="410" viewBox="0 0 430 410" fill="none" stroke="#cfd3dc" stroke-width="1"><circle cx="215" cy="200" r="160"/><circle cx="215" cy="200" r="120"/></svg>
  <div class="photo" role="img" aria-label="Doctors reviewing a laptop together" style="left:778px;top:58px;width:266px;height:208px;border-radius:6px;background:linear-gradient(135deg,#d9e3f0,#9fb3cf);box-shadow:0 10px 30px rgba(0,0,0,.12)"></div>
  <div class="photo" role="img" aria-label="Trainer presenting to medical staff" style="left:644px;top:223px;width:265px;height:221px;border-radius:6px;background:linear-gradient(135deg,#e6ecf4,#a9b9d2);box-shadow:0 10px 30px rgba(0,0,0,.12)"></div>
</section>

<section class="projects">
  <div class="label">Our Projects</div>
  <h2 class="abs title">Work We Have Done So Far</h2>
  <div class="photo" role="img" aria-label="Hospital room, faded" style="left:0;top:2701px;width:82px;height:313px;background:linear-gradient(135deg,#e5ebf4,#cbd6e6)"></div>
  <div class="photo" role="img" aria-label="Hospital room, faded" style="left:1117px;top:2701px;width:83px;height:313px;background:linear-gradient(135deg,#e5ebf4,#cbd6e6)"></div>
  <div class="circ" style="left:45px;top:3054px;background:#c7c9d1"><svg width="14" height="14" viewBox="0 0 14 14" fill="none" stroke="#fff" stroke-width="2"><path d="M2 7h10M8 3l4 4-4 4"/></svg></div>
  <h4 class="abs" style="left:1117px;top:3032px;font-size:22px;color:#cdd0dc;font-weight:600;width:83px;overflow:hidden;white-space:nowrap">Hospital</h4>

  <div class="proj">
    <div class="photo" role="img" aria-label="Operating room with imaging equipment" style="left:111px;top:2701px;width:473px;height:313px;background:linear-gradient(135deg,#eef0f3,#a5acb8 60%,#6b7380)"></div>
    <h4 style="left:111px">Hospital Name</h4>
    <p style="left:111px">Lorem ipsum dolor sit amet, consectetuer adipiscing elit, sed diam nonummy nibh euismod tincidunt ut laoreet dolore magna.</p>
    <div class="circ" style="left:548px;top:3054px;background:var(--navy)"><svg width="14" height="14" viewBox="0 0 14 14" fill="none" stroke="#fff" stroke-width="2"><path d="M2 7h10M8 3l4 4-4 4"/></svg></div>
  </div>
  <div class="proj">
    <div class="photo" role="img" aria-label="Patient inside a scanner with red laser lines" style="left:614px;top:2701px;width:473px;height:313px;background:radial-gradient(ellipse at 50% 55%,#c0313b,#5a1220 55%,#2a0a14)"></div>
    <h4 style="left:614px">Hospital Name</h4>
    <p style="left:614px">Lorem ipsum dolor sit amet, consectetuer adipiscing elit, sed diam nonummy nibh euismod tincidunt ut laoreet dolore magna.</p>
    <div class="circ" style="left:1050px;top:3054px;background:var(--navy)"><svg width="14" height="14" viewBox="0 0 14 14" fill="none" stroke="#fff" stroke-width="2"><path d="M2 7h10M8 3l4 4-4 4"/></svg></div>
  </div>
</section>

<section class="contact">
  <div class="photo" role="img" aria-label="Surgical team operating under theatre lights" style="inset:0"></div>
  <div class="form">
    <div class="label">Contact Us</div>
    <h2 class="title">Get In Touch With Us</h2>
    <div class="field" style="left:46px;top:133px;width:183px">First Name*</div>
    <div class="field" style="left:245px;top:133px;width:183px">Last Name*</div>
    <div class="field" style="left:46px;top:189px;width:183px">Email*</div>
    <div class="field" style="left:245px;top:189px;width:183px">Phone*</div>
    <div class="field" style="left:46px;top:245px;width:382px;height:87px">Message*</div>
    <div class="btn">Submit</div>
  </div>
</section>

<footer class="footer">
  <div class="brand"><span class="mark"></span>Zerovan Medical</div>
  <span class="social" style="left:127px;background:var(--blue);border-color:var(--blue)"></span>
  <span class="social" style="left:171px"></span>
  <span class="social" style="left:214px"></span>

  <div class="col" style="left:313px"><h4>Useful Links</h4><ul><li>About</li><li>Services</li><li>Training</li><li>Projects</li><li>Contact Us</li></ul></div>
  <div class="col" style="left:467px"><h4>Other Links</h4><ul><li>Support</li><li>Careers</li><li>Privacy Policy</li><li>Terms &amp; Conditions</li><li>Cookie Policy</li></ul></div>
  <div class="col" style="left:635px;width:200px">
    <h4>Contact Us</h4>
    <div class="contact-item"><svg width="14" height="18" viewBox="0 0 14 18" fill="none" stroke="var(--navy)" stroke-width="1.6"><path d="M7 17s6-6 6-10A6 6 0 0 0 1 7c0 4 6 10 6 10z"/><circle cx="7" cy="7" r="2"/></svg><div><b style="color:var(--navy);font-weight:600">Zerovan Medical</b><br><span style="font-size:11.5px">48 Harbor Lane, Kestrel District, Northvale - 10442</span></div></div>
    <div class="contact-item"><svg width="14" height="14" viewBox="0 0 24 24" fill="none" stroke="var(--navy)" stroke-width="2.4"><path d="M22 16.9v3a2 2 0 0 1-2.2 2A19.8 19.8 0 0 1 2.1 4.2 2 2 0 0 1 4.1 2h3a2 2 0 0 1 2 1.7c.1 1 .4 1.9.7 2.8a2 2 0 0 1-.5 2.1L8 9.9a16 16 0 0 0 6 6l1.3-1.3a2 2 0 0 1 2.1-.4c.9.3 1.8.6 2.8.7a2 2 0 0 1 1.7 2z"/></svg>(555) 014-8822</div>
    <div class="contact-item"><svg width="14" height="14" viewBox="0 0 16 12" fill="none" stroke="var(--navy)" stroke-width="1.5"><rect x="1" y="1" width="14" height="10"/><path d="M1 1l7 6 7-6"/></svg><u>info@zerovanmedical.com</u></div>
  </div>
  <div class="col" style="left:854px"><h4>Newsletter</h4><span style="font-size:11.5px">Subscribe To Our Newsletter Now!</span></div>
  <div class="news">Email*<b><svg width="16" height="16" viewBox="0 0 24 24" fill="none" stroke="#fff" stroke-width="2"><path d="M22 2L11 13M22 2l-7 20-4-9-9-4z"/></svg></b></div>

  <div class="bottom">©&nbsp;<b style="font-weight:600">Zerovan Medical</b>&nbsp;- 2024. All Rights Reserved.</div>
</footer>

</body>
</html>
```